card for handyman and landscaping business, double sided with services listed on the back

Design a business card for a handyman and Landscaping business in San Jose,ca. Would like front to be a house with 3D characters doing different tasks i.e. Mowing lawn, painting, sprinklers, lighting, weed whacking, power washing, lumber etc. on the backside a cutout of the interior with computer, internet, cleaning, bathroom/kitchen remodeling, smart home etc.

Industry/Entity Type

Handyman

Contact Information for Business Card

Two sided view of a house, one outside services and one inside services

Colors

Designer to choose colors to be used in the design.

Requirements
Must have
• General Household Repairs and Maintenance
• Landscaping, Gardening, and Planting
• Painting, Patching and Trim/Moulding Work
• Cleaning, Restoring and Hauling/Trash Removal
• Blinds, Curtains, and Assembly Work
• Computer, Internet/Wireless, and Smart Home Service

```html
<!DOCTYPE html>
<html lang="en">
<head>
<meta charset="utf-8">
<title>Home Maintenance Business Card</title>
<link rel="stylesheet" href="https://fonts.googleapis.com/css2?family=Cinzel:wght@400;600&family=Open+Sans:wght@400;600&display=swap">
<style>
  :root {
    --ink: #141414;
    --paper: #ffffff;
    --leaf: #76c043;
    --stage: #e3e9ec;
    --placeholder: #cfd6d2;
  }
  html, body {
    margin: 0;
    width: 1200px;
    height: 900px;
    overflow: hidden;
    background: var(--stage);
  }
  .sheet {
    position: relative;
    width: 1200px;
    height: 900px;
    display: flex;
    flex-direction: column;
    align-items: center;
    justify-content: center;
    gap: 28px;
  }
  .card {
    width: 640px;
    height: 366px;
    display: block;
    box-shadow: 0 10px 28px rgba(20, 30, 40, 0.18);
  }
  .display { font-family: "Cinzel", serif; }
  .body-text { font-family: "Open Sans", sans-serif; }
  .fill-ink { fill: var(--ink); }
  .fill-paper { fill: var(--paper); }
  .fill-leaf { fill: var(--leaf); }
  .stroke-leaf { stroke: var(--leaf); }
  .task-art { fill: var(--placeholder); }
</style>
</head>
<body>
<main class="sheet">

  <!-- Back side: services -->
  <svg class="card card-back" viewBox="0 0 640 366" xmlns="http://www.w3.org/2000/svg">
    <rect class="fill-ink" width="640" height="366"/>
    <polygon class="fill-leaf" points="0,250 70,118 640,92 640,114 0,276"/>
    <polygon class="fill-paper" points="0,366 0,276 82,140 640,114 640,366"/>

    <g class="brand-title display fill-leaf" text-anchor="end" font-size="19" font-weight="600">
      <text x="610" y="36">HOME</text>
      <text x="610" y="58">MAINTENANCE</text>
    </g>

    <g class="services">
      <text class="display fill-leaf" x="100" y="170" font-size="22" font-weight="600">SERVICES:</text>
      <line class="stroke-leaf" x1="100" y1="177" x2="230" y2="177" stroke-width="2"/>
      <g class="service-list body-text fill-ink" font-size="14">
        <g transform="translate(108,198)"><circle class="fill-leaf" cx="0" cy="-5" r="4"/><text x="12" y="0">General household repairs and maintenance</text></g>
        <g transform="translate(108,221)"><circle class="fill-leaf" cx="0" cy="-5" r="4"/><text x="12" y="0">Professional painter and decorator</text></g>
        <g transform="translate(108,244)"><circle class="fill-leaf" cx="0" cy="-5" r="4"/><text x="12" y="0">Gyprock/Plaster Repairs</text></g>
        <g transform="translate(108,267)"><circle class="fill-leaf" cx="0" cy="-5" r="4"/><text x="12" y="0">Fencing</text></g>
        <g transform="translate(108,290)"><circle class="fill-leaf" cx="0" cy="-5" r="4"/><text x="12" y="0">Gardening and landscaping</text></g>
        <g transform="translate(108,313)"><circle class="fill-leaf" cx="0" cy="-5" r="4"/><text x="12" y="0">Cleaning and removals</text></g>
        <g transform="translate(108,336)"><circle class="fill-leaf" cx="0" cy="-5" r="4"/><text x="12" y="0">Doors and windows</text></g>
      </g>
    </g>
  </svg>

  <!-- Front side: name and contact -->
  <svg class="card card-front" viewBox="0 0 640 366" xmlns="http://www.w3.org/2000/svg">
    <rect class="fill-ink" width="640" height="366"/>
    <polygon class="fill-leaf" points="28,366 150,168 640,214 640,236 48,366"/>
    <polygon class="fill-paper" points="50,366 162,190 640,236 640,366"/>

    <g class="identity">
      <text class="display fill-paper" x="600" y="72" text-anchor="end" font-size="36">DALE MERCER</text>
      <line class="stroke-leaf" x1="440" y1="86" x2="600" y2="86" stroke-width="2"/>
      <g class="contact body-text fill-paper" font-size="14" text-anchor="end">
        <text x="578" y="114">555.014.2280</text>
        <text x="578" y="138">555.014.7731</text>
        <text x="578" y="162">dale@mercerhandy.example</text>
      </g>
      <g class="contact-icons fill-leaf">
        <path d="M587 104 q4 -3 8 0 l3 3 q1 2 -1 3 l-2 1 q1 3 4 4 l1 -2 q1 -2 3 -1 l3 3 q2 4 -1 6 q-9 2 -18 -11 z"/>
        <rect x="588" y="130" width="16" height="9" rx="2"/>
        <rect x="591" y="125" width="10" height="5"/>
        <polygon points="587,156 606,149 598,166 595,159"/>
      </g>
    </g>

    <g class="tagline display fill-ink" font-size="21" font-weight="600">
      <text x="180" y="226">HANDYMAN,</text>
      <text x="180" y="250">LANDSCAPING,</text>
      <text x="180" y="274">AND TECH SERVICES</text>
    </g>
    <line class="stroke-leaf" x1="180" y1="286" x2="420" y2="286" stroke-width="2"/>

    <g class="task-icons" stroke-width="3">
      <g role="img" aria-label="Worker silhouette shovelling">
        <circle class="task-art stroke-leaf" cx="180" cy="330" r="24"/>
      </g>
      <g role="img" aria-label="Worker silhouette with wheelbarrow">
        <circle class="task-art stroke-leaf" cx="285" cy="330" r="24"/>
      </g>
      <g role="img" aria-label="Worker silhouette kneeling at a repair">
        <circle class="task-art stroke-leaf" cx="390" cy="330" r="24"/>
      </g>
      <g role="img" aria-label="Worker silhouette pushing a cart">
        <circle class="task-art stroke-leaf" cx="495" cy="330" r="24"/>
      </g>
      <g role="img" aria-label="Worker silhouette painting a wall">
        <circle class="task-art stroke-leaf" cx="595" cy="300" r="24"/>
      </g>
    </g>
  </svg>

</main>
</body>
</html>
```